Plivoro ( A new twist on task management )

We need modern, elegant, and clean (Material Design) on screens, buttons, and icons.

It is a (smart) task management application which helps the users to get notified and track task completion hassle free; Using notification profiles they create.

The interface of this application should be very simple and color schemes should be contemporary as long as they don’t make reading short text hard.

Following Material Design guidelines, the prefered font style is Roboto
Updates

Target Market(s)

Everyone from 13+

Industry/Entity Type

Software

Logo Text

Plivoro

Font styles to use
Other font styles liked:
• Roboto

```html
<!DOCTYPE html>
<html lang="en">
<head>
<meta charset="utf-8">
<title>Plivoro – New Profile</title>
<link rel="stylesheet" href="https://fonts.googleapis.com/css2?family=Roboto:wght@300;400;500&display=swap">
<style>
  :root {
    --stage: #a9a8ac;
    --primary: #1fa2d3;
    --primary-light: #35b3de;
    --accent: #f6918f;
    --accent-text: #f27d7a;
    --surface: #ffffff;
    --surface-muted: #f3f3f3;
    --divider: #e6e6e6;
    --text: #3d3d3d;
    --text-soft: #9a9a9a;
    --icon: #8c8c8c;
  }
  * { box-sizing: border-box; margin: 0; padding: 0; }
  html, body { width: 1200px; height: 864px; overflow: hidden; }
  body {
    background: var(--stage);
    font-family: "Roboto", sans-serif;
    color: var(--text);
    position: relative;
  }
  .screen {
    position: absolute;
    left: 400px; top: 24px;
    width: 400px; height: 816px;
    background: var(--surface-muted);
    display: flex; flex-direction: column;
    box-shadow: 0 18px 40px rgba(0,0,0,.25);
  }
  .app-bar {
    background: linear-gradient(90deg, var(--primary), var(--primary-light));
    color: #fff;
    height: 132px;
    position: relative;
  }
  .status-bar {
    height: 26px;
    display: flex; justify-content: flex-end; align-items: center;
    gap: 8px; padding-right: 14px;
    font-size: 12px;
  }
  .status-bar svg { fill: #fff; }
  .filter-button { position: absolute; right: 16px; top: 40px; }
  .profile {
    position: absolute; left: 18px; bottom: 18px;
    display: flex; align-items: center; gap: 14px;
  }
  .avatar {
    width: 52px; height: 52px; border-radius: 50%;
    background: radial-gradient(circle at 40% 40%, #c9a57a, #5b4a3c);
    border: 2px solid rgba(255,255,255,.6);
  }
  .profile-name { font-size: 20px; font-weight: 500; }
  .tasks-strip {
    background: var(--surface);
    padding: 10px 16px 14px;
    text-align: center;
  }
  .tasks-title { color: var(--accent-text); font-size: 17px; margin-bottom: 8px; }
  .search-field { height: 38px; border: 1px solid var(--divider); border-radius: 3px; }
  .profile-card {
    background: var(--surface);
    margin-top: 10px;
    padding: 14px 16px 0;
  }
  .text-field {
    height: 44px; border: 1px solid var(--divider); border-radius: 3px;
    display: flex; align-items: center; padding-left: 14px;
    color: var(--text-soft); font-size: 17px;
  }
  .trigger-tabs { display: flex; margin: 14px -16px 0; }
  .trigger-tab {
    flex: 1; height: 48px; display: flex; align-items: center; justify-content: center;
    font-size: 16px; color: var(--text-soft);
  }
  .trigger-tab.is-active { background: var(--accent); color: #fff; }
  .toggle-row { display: flex; justify-content: flex-end; padding: 10px 0 6px; }
  .toggle { display: flex; border: 1px solid var(--primary); border-radius: 3px; overflow: hidden; font-size: 12px; }
  .toggle span { width: 46px; height: 22px; display: flex; align-items: center; justify-content: center; }
  .toggle .off { color: var(--text-soft); }
  .toggle .on { background: var(--primary); color: #fff; }
  .setting-row {
    height: 62px; display: flex; align-items: center; justify-content: space-between;
    border-top: 1px solid var(--divider);
    font-size: 18px;
  }
  .time-range { display: flex; align-items: center; gap: 8px; font-size: 18px; }
  .time-input { width: 62px; border-bottom: 1px solid var(--divider); height: 14px; }
  .spacer { flex: 1; }
  .action-bar {
    height: 96px; background: var(--surface);
    display: flex; align-items: center;
  }
  .action { flex: 1; display: flex; justify-content: center; }
  .action-divider { width: 1px; height: 48px; background: var(--divider); }
  .icon { stroke: var(--icon); fill: none; stroke-width: 1.4; }
</style>
</head>
<body>
<main class="screen">
  <header class="app-bar">
    <div class="status-bar">
      <svg width="14" height="12" viewBox="0 0 14 12"><path d="M0 2 Q7 -2 14 2 L7 12Z"/></svg>
      <svg width="12" height="12" viewBox="0 0 12 12"><path d="M12 0V12H0Z"/></svg>
      <svg width="8" height="13" viewBox="0 0 8 13"><rect x="0" y="1" width="8" height="12" rx="1"/></svg>
      <span>12:30</span>
    </div>
    <svg class="filter-button" width="26" height="22" viewBox="0 0 26 22" stroke="#fff" stroke-width="1.5" fill="none">
      <line x1="1" y1="4" x2="25" y2="4"/><circle cx="8" cy="4" r="2.5" fill="#1fa2d3"/>
      <line x1="1" y1="11" x2="25" y2="11"/><circle cx="18" cy="11" r="2.5" fill="#1fa2d3"/>
      <line x1="1" y1="18" x2="25" y2="18"/><circle cx="11" cy="18" r="2.5" fill="#1fa2d3"/>
    </svg>
    <div class="profile">
      <div class="avatar" role="img" aria-label="User profile photo"></div>
      <span class="profile-name">Dev Halloran</span>
    </div>
  </header>

  <section class="tasks-strip">
    <h2 class="tasks-title">Active Tasks</h2>
    <div class="search-field"></div>
  </section>

  <section class="profile-card">
    <div class="text-field">Enter Profile Name</div>
    <div class="trigger-tabs">
      <div class="trigger-tab">Location</div>
      <div class="trigger-tab is-active">Time</div>
    </div>
    <div class="toggle-row">
      <div class="toggle"><span class="off">Off</span><span class="on">On</span></div>
    </div>
    <div class="setting-row">
      <span>Time Trigger</span>
      <svg class="icon" width="24" height="24" viewBox="0 0 24 24"><rect x="2" y="4" width="20" height="18" rx="1"/><line x1="2" y1="9" x2="22" y2="9"/><line x1="7" y1="2" x2="7" y2="6"/><line x1="17" y1="2" x2="17" y2="6"/><path d="M6 13h2M11 13h2M16 13h2M6 17h2M11 17h2M16 17h2"/></svg>
    </div>
    <div class="setting-row">
      <span>Set Start Day</span>
      <svg class="icon" width="22" height="14" viewBox="0 0 22 14"><path d="M2 3 L11 11 L20 3"/></svg>
    </div>
    <div class="setting-row">
      <span>Repeat Every</span>
      <svg class="icon" width="24" height="24" viewBox="0 0 24 24"><circle cx="12" cy="12" r="10"/><path d="M12 6v6h-4"/></svg>
    </div>
    <div class="setting-row">
      <span>Between</span>
      <div class="time-range">
        <span class="time-input"></span>
        <svg class="icon" width="24" height="24" viewBox="0 0 24 24"><circle cx="12" cy="12" r="10"/><path d="M12 6v6h-4"/></svg>
        <span>and</span>
        <span class="time-input"></span>
        <svg class="icon" width="24" height="24" viewBox="0 0 24 24"><circle cx="12" cy="12" r="10"/><path d="M12 6v6h-4"/></svg>
      </div>
    </div>
  </section>

  <div class="spacer"></div>

  <footer class="action-bar">
    <button class="action" aria-label="Cancel" style="background:none;border:0">
      <svg class="icon" width="28" height="28" viewBox="0 0 28 28"><path d="M4 4 L24 24 M24 4 L4 24"/></svg>
    </button>
    <span class="action-divider"></span>
    <button class="action" aria-label="Save" style="background:none;border:0">
      <svg class="icon" width="28" height="28" viewBox="0 0 28 28"><path d="M4 15 L11 22 L24 6"/></svg>
    </button>
  </footer>
</main>
</body>
</html>
```